Webdesign für Anbieter von Erotik-Geschichten
Zielgruppe
Wir sind ein Anbieter von Erotik-Geschichten. Die Marke heisst Lunvo Erotica. Das Erlebnis für die Kunden soll hochwertig und persönlich wirken. Daher in keiner Art und Weise schmuddelig. Die Zielgruppe sind Frauen ab ca. 20-40. Die Geschichten werden frei lesbar sein, d.h. es ist kein Online-Shop sondern mehr eine Art Blog mit verschiedenen Geschichten.
Aufgabenstellung
Wichtig ist uns eine schlichtes, minimalistisches Design (vrgl. Tafelwerk) aber trotzdem hochwertig (leicht luxuriös) wirkend.

```html
<!DOCTYPE html>
<html lang="de">
<head>
<meta charset="utf-8">
<title>Lunvo – Zufälle und Konsequenzen</title>
<link rel="stylesheet" href="https://fonts.googleapis.com/css2?family=Bitter:wght@400;500;600;700&family=Open+Sans:wght@400;600;700&display=swap">
<style>
  :root{
    --bg:#2e2e2e;
    --bg-header:#2a2a2a;
    --ink:#ffffff;
    --ink-soft:#e9e9e9;
    --muted:#a9a9a9;
    --accent:#d9271f;
    --serif:"Bitter", Georgia, serif;
    --sans:"Open Sans", Arial, sans-serif;
  }
  *{box-sizing:border-box;margin:0;padding:0}
  html,body{width:1200px;height:2718px;overflow:hidden;background:var(--bg)}
  body{position:relative;font-family:var(--sans);color:var(--ink)}
  a{color:inherit}

  .site-header{position:absolute;left:0;top:0;width:1200px;height:116px;background:var(--bg-header)}
  .brand{position:absolute;left:74px;top:40px;font-family:var(--serif);font-size:32px;font-weight:500;color:var(--ink);text-decoration:none;letter-spacing:.5px}
  .main-nav{position:absolute;top:54px;left:252px;display:flex;gap:0}
  .main-nav a{position:absolute;font-family:var(--serif);font-size:14px;font-weight:500;letter-spacing:.4px;text-decoration:none;color:var(--ink);white-space:nowrap}
  .main-nav a.is-active{color:var(--accent)}
  .header-tools{position:absolute;top:0;left:0}
  .tool-icon{position:absolute;top:52px;width:18px;height:18px;fill:var(--accent)}
  .btn-upgrade{position:absolute;left:953px;top:44px;width:114px;height:33px;border:2px solid var(--accent);border-radius:17px;color:var(--accent);font-family:var(--serif);font-weight:600;font-size:15px;display:flex;align-items:center;justify-content:center;text-decoration:none}
  .user-avatar{position:absolute;left:1084px;top:44px;width:37px;height:37px;border-radius:50%;border:2px solid var(--accent);background:radial-gradient(circle at 50% 45%,#c99a82,#6b4a3c 70%)}

  .category-hero{position:absolute;left:0;top:116px;width:1200px;height:234px;
    background:linear-gradient(90deg,#2f2d2b 0%,#5b5046 18%,#1c1816 24%,#2b2320 45%,#8c6a58 62%,#3a2a24 78%,#9a4a1e 92%,#c0682c 100%)}
  .category-hero h1{position:absolute;left:251px;top:82px;font-family:var(--serif);font-weight:500;font-size:58px;color:var(--accent);letter-spacing:1px}

  .breadcrumb{position:absolute;left:252px;top:368px;font-size:13px;color:var(--muted);display:flex;gap:14px}
  .breadcrumb a{text-decoration:underline}
  .breadcrumb .sep{color:var(--accent)}

  .article{position:absolute;left:253px;top:0;width:710px}
  .article-title{position:absolute;top:428px;left:-3px;white-space:nowrap;font-family:var(--serif);font-weight:400;font-size:43px;color:var(--ink)}
  .article-lead{position:absolute;top:496px;width:640px;font-family:var(--serif);font-size:28px;line-height:43px;color:var(--ink)}

  .author{position:absolute;top:648px;left:-4px}
  .author-avatar{position:absolute;left:0;top:0;width:55px;height:55px;border-radius:50%;border:2px solid var(--accent);background:radial-gradient(circle at 50% 45%,#d8a996,#5a2a2a 72%)}
  .author-name{position:absolute;left:71px;top:7px;font-size:14.5px;white-space:nowrap}
  .author-meta{position:absolute;left:71px;top:27px;font-size:14.5px;white-space:nowrap}
  .btn-follow{position:absolute;left:70px;top:56px;width:70px;height:25px;border:2px solid var(--accent);border-radius:13px;color:var(--accent);font-family:var(--serif);font-weight:600;font-size:11px;display:flex;align-items:center;justify-content:center}

  .body-text{position:absolute;width:705px;font-size:18.5px;line-height:31.8px;color:var(--ink-soft)}
  .pull-quote{position:absolute;left:74px;top:1071px;width:500px;border-left:2px solid var(--accent);padding-left:13px;font-family:var(--serif);font-size:25px;line-height:38.5px;color:var(--accent)}
  .article-image{position:absolute;top:1676px;left:0;width:599px;height:375px;background:linear-gradient(135deg,#8a8a8a 0%,#3a3a3a 35%,#1d1d1d 55%,#b9b9b9 80%,#5d5d5d 100%)}
  .btn-more{position:absolute;left:6px;top:2397px;width:236px;height:44px;border:2px solid var(--ink);border-radius:22px;font-family:var(--serif);font-weight:700;font-size:20px;display:flex;align-items:center;justify-content:center;color:var(--ink)}

  .site-footer{position:absolute;left:0;top:2519px;width:1200px;height:199px;border-top:2px solid var(--accent)}
  .footer-nav a{position:absolute;top:20px;font-family:var(--serif);font-size:14px;font-weight:500;letter-spacing:.4px;text-decoration:none;white-space:nowrap}
  .footer-brand{position:absolute;left:0;width:1200px;top:74px;text-align:center;font-family:var(--serif);font-size:44px;font-weight:500}
  .footer-legal{font-size:11px;font-weight:700;color:var(--muted)}
  .footer-legal span,.footer-legal a{position:absolute;top:174px;white-space:nowrap}
</style>
</head>
<body>
  <header class="site-header">
    <a class="brand" href="#">Lunvo</a>
    <nav class="main-nav">
      <a href="#" style="left:0">HOME</a>
      <a href="#" class="is-active" style="left:78px">KATEGORIEN</a>
      <a href="#" style="left:206px">AUTOREN</a>
      <a href="#" style="left:308px">ÜBER UNS</a>
    </nav>
    <svg class="tool-icon" style="left:838px" viewBox="0 0 20 20" aria-label="Suche"><circle cx="8" cy="8" r="5.5" fill="none" stroke="#d9271f" stroke-width="3"/><path d="M12 12l6 6" stroke="#d9271f" stroke-width="3.2" stroke-linecap="round"/></svg>
    <svg class="tool-icon" style="left:878px" viewBox="0 0 20 20" aria-label="Merkliste"><path d="M4 1h12v18l-6-5-6 5z"/></svg>
    <svg class="tool-icon" style="left:915px" viewBox="0 0 20 20" aria-label="Mitteilungen"><path d="M10 1c-3.5 0-6 2.7-6 6.5V12l-2 3h16l-2-3V7.5C16 3.7 13.5 1 10 1z"/><circle cx="10" cy="17.5" r="2"/></svg>
    <a class="btn-upgrade" href="#">Upgrade</a>
    <div class="user-avatar" role="img" aria-label="Profilbild des Nutzers"></div>
  </header>

  <section class="category-hero" role="img" aria-label="Kategoriebild: Hände in ledernen Handfesseln mit Kette">
    <h1>BDSM</h1>
  </section>

  <nav class="breadcrumb">
    <a href="#">Start</a><span class="sep">&gt;</span>
    <a href="#">Kategorien</a><span class="sep">&gt;</span>
    <a href="#">BDSM</a><span class="sep">&gt;</span>
    <span>Zufälle und Konsequenzen</span>
  </nav>

  <article class="article">
    <h2 class="article-title">Zufälle und Konsequenzen</h2>
    <p class="article-lead">Der unbewohnte kleine Hof, am Rande des Städtchens, war heruntergekommen und schon ziemlich verfallen.</p>

    <div class="author">
      <div class="author-avatar" role="img" aria-label="Porträt der Autorin"></div>
      <div class="author-name">Mira von Falk</div>
      <div class="author-meta">12 April 2021 - 6 min Lesezeit</div>
      <div class="btn-follow">Folgen</div>
    </div>

    <p class="body-text" style="top:782px">Lorem ipsum dolor sit amet, consectetuer adipiscing elit. Aenean commodo ligula eget dolor. Aenean massa. Cum sociis natoque penatibus et magnis dis parturient montes, nascetur ridiculus mus. Donec quam felis, ultricies nec, pellentesque eu, pretium quis, sem. Nulla consequat massa quis enim. Donec pede justo, fringilla vel, aliquet nec, vulputate eget, arcu. In enim justo, rhoncus ut, imperdiet a, venenatis vitae, justo. Nullam dictum felis eu pede mollis pretium. Integer tincidunt. Cras dapibus. Vivamus</p>

    <blockquote class="pull-quote">Um sie herum standen vereinzelte Menschen, Paare, Gruppen – allesamt waren sie mit sich selbst oder gegenseitig beschäftigt.</blockquote>

    <p class="body-text" style="top:1277px">elementum semper nisi. Aenean vulputate eleifend tellus. Aenean leo ligula, porttitor eu, consequat vitae, eleifend ac, enim. Aliquam lorem ante, dapibus in, viverra quis, feugiat a, tellus. Phasellus viverra nulla ut metus varius laoreet. Quisque rutrum. Aenean imperdiet. Etiam ultricies nisi vel augue. Curabitur ullamcorper ultricies nisi. Nam eget dui. Etiam rhoncus. Maecenas tempus, tellus eget condimentum rhoncus, sem quam semper libero, sit amet adipiscing sem neque sed ipsum. Nam quam nunc, blandit vel, luctus pulvinar, hendrerit id, lorem. Maecenas nec odio et ante tincidunt tempus. Donec vitae sapien ut libero venenatis faucibus. Nullam quis ante. Etiam sit amet orci eget eros faucibus tincidunt. Duis leo. Sed fringilla mauris sit amet nibh. Donec sodales sagittis magna. Sed consequat, leo eget bibendum sodales, augue velit cursus nunc, quis</p>

    <div class="article-image" role="img" aria-label="Schwarz-Weiß-Foto: Paar in Spitzenwäsche in inniger Umarmung"></div>

    <p class="body-text" style="top:2103px">Nam pretium turpis et arcu. Duis arcu tortor, suscipit eget, imperdiet nec, imperdiet iaculis, ipsum. Sed aliquam ultrices mauris. Integer ante arcu, accumsan a, consectetuer eget, posuere ut, mauris. Praesent adipiscing. Phasellus ullamcorper ipsum rutrum nunc. Nunc nonummy metus. Vestibulum volutpat pretium libero. Cras id dui. Aenean ut eros et nisl sagittis vestibulum. Nullam nulla eros, ultricies sit amet, nonummy id, imperdiet feugiat, pede. Sed lectus. Donec mollis hendrerit risus. Phasellus nec sem in justo pellentesque facilisis. Etiam imperdiet imperdiet orci. Nunc nec neque. Phasellus leo dolo</p>

    <div class="btn-more">Weiter lesen</div>
  </article>

  <footer class="site-footer">
    <nav class="footer-nav">
      <a href="#" style="left:405px">HOME</a>
      <a href="#" style="left:483px">KATEGORIEN</a>
      <a href="#" style="left:610px">AUTOREN</a>
      <a href="#" style="left:714px">ÜBER UNS</a>
    </nav>
    <div class="footer-brand">Lunvo</div>
    <div class="footer-legal">
      <span style="left:364px">© Lunvo GmbH 2021</span>
      <a href="#" style="left:535px">Impressum</a>
      <a href="#" style="left:661px">AGB</a>
      <a href="#" style="left:743px">Datenschutz</a>
    </div>
  </footer>
</body>
</html>
```